KORBALT

The business want a professional looking business card. We have a scetch we will add but want the extra upgrade, and would like more suggestions for variations of our business cards.

```html
<!DOCTYPE html>
<html lang="en">
<head>
<meta charset="utf-8">
<title>KORBALT Business Card</title>
<link href="https://fonts.googleapis.com/css2?family=Cormorant+Garamond:wght@600&family=Barlow+Semi+Condensed:wght@600&family=Arimo&display=swap" rel="stylesheet">
<style>
  :root {
    --gold: #8b6d3d;
    --paper: #ffffff;
  }
  * { margin: 0; padding: 0; box-sizing: border-box; }
  html, body { width: 1200px; height: 550px; overflow: hidden; background: var(--paper); }
  .canvas { position: relative; width: 1200px; height: 550px; }

  .card { position: absolute; top: 87px; width: 533px; height: 326px; }
  .card-front { left: 49px; border: 2px solid var(--gold); background: var(--paper); color: var(--gold); }
  .card-back { left: 598px; background: var(--gold); color: var(--paper); }

  .brand-dot { position: absolute; border-radius: 50%; }
  .card-front .brand-dot { left: 394px; top: 55px; width: 56px; height: 56px; background: var(--gold); }
  .card-back .brand-dot { left: 223px; top: 88px; width: 90px; height: 90px; background: var(--paper); }

  .brand-name {
    position: absolute; text-align: center; white-space: nowrap;
    font-family: "Cormorant Garamond", serif; font-weight: 600; letter-spacing: 0.5px; line-height: 1;
  }
  .card-front .brand-name { left: 322px; width: 200px; top: 143px; font-size: 31px; }
  .card-back .brand-name { left: 116px; width: 300px; top: 217px; font-size: 46px; }

  .brand-since {
    position: absolute; text-align: center; white-space: nowrap;
    font-family: "Barlow Semi Condensed", sans-serif; font-weight: 600; letter-spacing: 0.5px; line-height: 1;
  }
  .card-front .brand-since { left: 322px; width: 200px; top: 175px; font-size: 10px; }
  .card-back .brand-since { left: 116px; width: 300px; top: 267px; font-size: 16px; }

  .person-name {
    position: absolute; left: 27px; top: 191px; white-space: nowrap;
    font-family: "Cormorant Garamond", serif; font-weight: 600; font-size: 31px; line-height: 1;
  }
  .person-role {
    position: absolute; left: 28px; top: 218px;
    font-family: "Arimo", sans-serif; font-size: 16px; line-height: 1;
  }
  .divider { position: absolute; left: 28px; top: 235px; width: 475px; height: 1px; background: var(--gold); }

  .contact {
    position: absolute; display: flex; align-items: center; gap: 5px;
    font-family: "Arimo", sans-serif; font-size: 14px; line-height: 1; white-space: nowrap;
  }
  .contact svg { display: block; }
  .contact-phone { left: 30px; top: 261px; }
  .contact-email { left: 28px; top: 282px; }
  .contact-web { right: 28px; top: 282px; }
</style>
</head>
<body>
<div class="canvas">

  <section class="card card-front">
    <div class="brand-dot"></div>
    <div class="brand-name">KORBALT F</div>
    <div class="brand-since">SINCE 2026</div>

    <div class="person-name">KORBALT F VINDHOLM</div>
    <div class="person-role">CEO &amp; Founder</div>
    <div class="divider"></div>

    <div class="contact contact-phone">
      <svg width="9" height="14" viewBox="0 0 9 14"><rect x="0.7" y="0.7" width="7.6" height="12.6" rx="1.5" fill="none" stroke="#8b6d3d" stroke-width="1.2"/><line x1="3" y1="11.3" x2="6" y2="11.3" stroke="#8b6d3d" stroke-width="1"/></svg>
      <span>004791458270</span>
    </div>
    <div class="contact contact-email">
      <svg width="12" height="9" viewBox="0 0 12 9"><rect x="0" y="0" width="12" height="9" fill="#8b6d3d"/><polyline points="0.5,0.5 6,5 11.5,0.5" fill="none" stroke="#fff" stroke-width="1"/><line x1="0.5" y1="8.5" x2="4.5" y2="4" stroke="#fff" stroke-width="0.8"/><line x1="11.5" y1="8.5" x2="7.5" y2="4" stroke="#fff" stroke-width="0.8"/></svg>
      <span>korbalt.llc@mailpost.com</span>
    </div>
    <div class="contact contact-web">
      <svg width="11" height="11" viewBox="0 0 12 12"><g fill="none" stroke="#8b6d3d" stroke-width="1"><circle cx="6" cy="6" r="5.3"/><ellipse cx="6" cy="6" rx="2.4" ry="5.3"/><line x1="0.7" y1="6" x2="11.3" y2="6"/><line x1="1.6" y1="3.3" x2="10.4" y2="3.3"/><line x1="1.6" y1="8.7" x2="10.4" y2="8.7"/></g></svg>
      <span>www.korbalt.llc</span>
    </div>
  </section>

  <section class="card card-back">
    <div class="brand-dot"></div>
    <div class="brand-name">KORBALT F</div>
    <div class="brand-since">SINCE 2026</div>
  </section>

</div>
</body>
</html>
```